Building company needs a letterhead design

I'm after a modern but professional letter head.
Must have the below details:
- Logo
- Website - TARVELGROUP.COM.AU
- Email - INFO@TARVELGROUP.COM.AU
- Office - 03 58206317
- Mobile number - 0413865290
- ABN - 47 318 264 105
...........................................................................................................................................................................................................................
- Logo
- Office - 03 58206317
- ABN - 47 318 264 105

Target Market(s)

.

Industry/Entity Type

Construction Company

Font styles to use
Sans Serif

Requirements
Must have
• Must have the below details:
• - Logo
• - Website - TARVELGROUP.COM.AU
• - Email - INFO@TARVELGROUP.COM.AU
• - Office - 03 58206317
• - Mobile number - 0413865290
• - ABN - 47 318 264 105
Nice to have
• .
Should not have
• .

```html
<!DOCTYPE html>
<html lang="en">
<head>
<meta charset="utf-8">
<title>Tarvel Building Group – Letterhead</title>
<link href="https://fonts.googleapis.com/css2?family=Open+Sans:wght@400;700;800&display=swap" rel="stylesheet">
<style>
  :root {
    --backdrop: #e9e9ea;
    --paper: #f7f7f8;
    --brand-yellow: #e9a800;
    --brand-charcoal: #545454;
    --text-grey: #555a5f;
    --rule-grey: #b9b9bb;
    --rule-yellow: #f0d58a;
  }
  * { margin: 0; padding: 0; box-sizing: border-box; }
  html, body {
    width: 1200px; height: 1192px; overflow: hidden;
    background: var(--backdrop);
    font-family: "Open Sans", Arial, sans-serif;
  }
  .letterhead {
    position: absolute; left: 211px; top: 46px;
    width: 778px; height: 1100px;
    background: var(--paper);
    box-shadow: 0 2px 10px rgba(0,0,0,0.08);
  }
  .side-band { position: absolute; left: 0; top: 0; }
  .brand {
    position: absolute; left: 56px; top: 70px;
    display: flex; align-items: center; gap: 12px;
  }
  .brand-mark { width: 38px; height: 38px; background: var(--brand-yellow); }
  .brand-name {
    color: var(--brand-yellow); font-weight: 800;
    font-size: 21px; line-height: 1.05; letter-spacing: 0.5px;
  }
  .brand-name small { display: block; font-size: 13px; letter-spacing: 1.4px; }
  .header-rule {
    position: absolute; left: 300px; right: 38px; top: 122px;
    height: 1px; background: var(--rule-yellow);
  }
  .footer-rule {
    position: absolute; left: 80px; right: 38px; top: 958px;
    height: 1px; background: var(--rule-grey);
  }
  .contact {
    position: absolute; top: 985px;
    display: flex; gap: 12px;
    font-size: 12px; line-height: 18px; color: var(--text-grey);
  }
  .contact-phones { left: 80px; }
  .contact-online { left: 260px; }
  .contact-icons { display: flex; flex-direction: column; gap: 4px; padding-top: 2px; }
  .contact-icons svg { width: 14px; height: 14px; fill: var(--brand-yellow); }
  .abn {
    position: absolute; left: 540px; top: 1025px;
    font-size: 13px; color: var(--text-grey);
  }
  .abn-label { color: var(--brand-yellow); }
</style>
</head>
<body>
  <main class="letterhead">
    <svg class="side-band" width="30" height="1100" viewBox="0 0 30 1100" aria-hidden="true">
      <polygon points="0,0 24,0 24,628 0,648" fill="var(--brand-yellow)"/>
      <polygon points="0,668 24,648 24,752 0,772" fill="var(--brand-charcoal)"/>
      <polygon points="0,792 24,772 24,846 0,866" fill="var(--brand-yellow)"/>
      <polygon points="0,886 24,866 24,990 0,1010" fill="var(--brand-charcoal)"/>
    </svg>

    <header class="brand">
      <span class="brand-mark"></span>
      <div class="brand-name">TARVEL<small>BUILDING GROUP</small></div>
    </header>
    <div class="header-rule"></div>

    <div class="footer-rule"></div>

    <div class="contact contact-phones">
      <div class="contact-icons">
        <svg viewBox="0 0 16 16"><path d="M3 1h3l1.5 4-2 1.3a9 9 0 0 0 4.2 4.2L11 8.5l4 1.5v3a2 2 0 0 1-2 2A12 12 0 0 1 1 3a2 2 0 0 1 2-2z"/></svg>
        <svg viewBox="0 0 16 16"><path d="M4.5 0h7a1.5 1.5 0 0 1 1.5 1.5v13a1.5 1.5 0 0 1-1.5 1.5h-7A1.5 1.5 0 0 1 3 14.5v-13A1.5 1.5 0 0 1 4.5 0zM5 2v10h6V2zm3 11a1 1 0 1 0 0 2 1 1 0 0 0 0-2z"/></svg>
      </div>
      <div>03 58206317<br>0413865290</div>
    </div>

    <div class="contact contact-online">
      <div class="contact-icons">
        <svg viewBox="0 0 16 16"><path d="M1 3h14v10H1zm1.5 1.2V12h11V4.2L8 8.6z M2.8 4L8 7.6 13.2 4z"/></svg>
        <svg viewBox="0 0 16 16"><path d="M8 0a8 8 0 1 0 0 16A8 8 0 0 0 8 0zm5.9 7h-2.6a12 12 0 0 0-1.2-5A6 6 0 0 1 13.9 7zM8 2c.8 1 1.6 2.7 1.8 5H6.2C6.4 4.7 7.2 3 8 2zM5.9 2a12 12 0 0 0-1.2 5H2.1A6 6 0 0 1 5.9 2zM2.1 9h2.6a12 12 0 0 0 1.2 5A6 6 0 0 1 2.1 9zM8 14c-.8-1-1.6-2.7-1.8-5h3.6C9.6 11.3 8.8 13 8 14zm2.1 0a12 12 0 0 0 1.2-5h2.6a6 6 0 0 1-3.8 5z"/></svg>
      </div>
      <div>info@tarvelgroup.com.au<br>www.tarvelgroup.com.au</div>
    </div>

    <p class="abn"><span class="abn-label">ABN</span> : 47 318 264 105</p>
  </main>
</body>
</html>
```